New Business Card Design Project

double sided business cards. i would like to design a business card with the logo attached . that logo being centered on 1 side and then my info on the other.

Boyd Whitfield CEO
Phone# 334-571-2806
Boyd@brightoakupkeep.com

Contact Information for Business Card

double sided one side the Logo attached below that saying Home Maintenance and Repair Specialists then on back my info Boyd Whitfield CEO Home Maintenance Specialist Phone# 334-571-2806 Boyd@brightoakupkeep.com

Font styles to use
Serif

Colors
0054AA
0677BA
7BADD7
CADEEF
E8F1F8
FFC000
F8CF3A
FAE287
FDF2CF
FEFAEE

Requirements
Must have
• double sided logo attached on one side with colors blue and gold. black background info on the other side

```html
<!DOCTYPE html>
<html lang="en">
<head>
<meta charset="utf-8">
<title>Bright Oak Upkeep – Business Card</title>
<link href="https://fonts.googleapis.com/css2?family=Urbanist:wght@400;500;600;700&display=swap" rel="stylesheet">
<style>
  :root {
    --page: #2a2c30;
    --card: #000000;
    --blue: #1f74c8;
    --blue-deep: #0054aa;
    --gold: #ffc000;
    --white: #f2f2f2;
    --grey: #cfcfcf;
    --faint: #2b2b2b;
  }
  * { margin: 0; padding: 0; box-sizing: border-box; }
  html, body { width: 1200px; height: 900px; overflow: hidden; }
  body {
    background: var(--page);
    font-family: "Urbanist", sans-serif;
    display: flex;
    flex-direction: column;
    align-items: center;
    justify-content: center;
    gap: 56px;
  }
  .card {
    position: relative;
    width: 640px;
    height: 366px;
    background: var(--card);
    border: 5px solid var(--blue);
    overflow: hidden;
  }

  /* Front side */
  .front {
    display: flex;
    flex-direction: column;
    align-items: center;
    justify-content: center;
    gap: 34px;
  }
  .brand {
    display: flex;
    align-items: center;
    gap: 14px;
    color: var(--blue);
    font-weight: 700;
    letter-spacing: 1px;
    text-transform: uppercase;
  }
  .brand-dot { background: var(--gold); border-radius: 50%; }
  .front .brand { font-size: 46px; }
  .front .brand-dot { width: 22px; height: 22px; }
  .front-phone {
    display: flex;
    align-items: center;
    gap: 14px;
    color: var(--white);
    font-size: 17px;
    letter-spacing: 1.5px;
  }
  .front-phone .rule { width: 74px; height: 1px; background: var(--white); }

  /* Back side */
  .back .brand {
    position: absolute;
    left: 36px;
    top: 34px;
    font-size: 26px;
  }
  .back .brand-dot { width: 14px; height: 14px; }
  .contact-list {
    position: absolute;
    left: 36px;
    top: 96px;
    list-style: none;
    display: flex;
    flex-direction: column;
    gap: 14px;
    color: var(--grey);
    font-size: 15px;
  }
  .contact-list li { display: flex; align-items: center; gap: 12px; }
  .contact-icon { width: 20px; height: 20px; flex: none; }
  .holder {
    position: absolute;
    right: 40px;
    top: 190px;
    text-align: right;
  }
  .holder-name { color: var(--blue); font-size: 27px; font-weight: 500; }
  .holder-role { color: var(--white); font-size: 15px; font-weight: 600; margin-top: 2px; }
  .edge-tab {
    position: absolute;
    right: 0;
    top: 246px;
    width: 20px;
    height: 46px;
    background: var(--blue);
  }
  .watermark-name {
    position: absolute;
    right: 120px;
    bottom: 60px;
    color: var(--faint);
    font-size: 40px;
    font-weight: 700;
    text-transform: uppercase;
  }
  .base-band {
    position: absolute;
    left: 0; right: 0; bottom: 0;
    height: 30px;
    background: var(--blue);
  }
  .gold-line {
    position: absolute;
    bottom: 40px;
    height: 4px;
    background: var(--gold);
  }
  .gold-line.long { left: 0; width: 300px; }
  .gold-line.short { right: 0; width: 40px; }
  .band-label {
    position: absolute;
    left: 318px;
    bottom: 34px;
    color: var(--white);
    font-size: 12px;
    font-weight: 600;
    letter-spacing: .5px;
    text-transform: uppercase;
  }
</style>
</head>
<body>

  <section class="card front" aria-label="Card front">
    <div class="brand"><span class="brand-dot"></span>Bright Oak Upkeep</div>
    <div class="front-phone"><span class="rule"></span>334-571-2806<span class="rule"></span></div>
  </section>

  <section class="card back" aria-label="Card back">
    <div class="brand"><span class="brand-dot"></span>Bright Oak Upkeep</div>

    <ul class="contact-list">
      <li>
        <svg class="contact-icon" viewBox="0 0 20 20" aria-hidden="true">
          <circle cx="10" cy="10" r="9" fill="none" stroke="var(--blue)" stroke-width="1.5"/>
          <path d="M7 5.5c-.8.5-1 1.6-.4 3 .8 1.9 2.6 3.8 4.6 4.9 1.3.7 2.4.6 2.9-.2l-1.6-1.6-1.2.6c-1-.6-1.9-1.5-2.5-2.5l.6-1.2L7.8 5z" fill="var(--blue)"/>
        </svg>
        334-571-2806
      </li>
      <li>
        <svg class="contact-icon" viewBox="0 0 20 20" aria-hidden="true">
          <circle cx="10" cy="10" r="9" fill="none" stroke="var(--blue)" stroke-width="1.5"/>
          <rect x="5.5" y="6.5" width="9" height="7" fill="var(--blue)"/>
          <path d="M5.5 6.8 10 10.5l4.5-3.7" fill="none" stroke="#000" stroke-width="1"/>
        </svg>
        Boyd@brightoakupkeep.com
      </li>
    </ul>

    <div class="holder">
      <p class="holder-name">Boyd Whitfield</p>
      <p class="holder-role">CEO</p>
    </div>
    <span class="edge-tab"></span>

    <div class="watermark-name" aria-hidden="true">Bright Oak</div>

    <span class="gold-line long"></span>
    <span class="band-label">Bright Oak Upkeep</span>
    <span class="gold-line short"></span>
    <span class="base-band"></span>
  </section>

</body>
</html>
```